Veltarum

Standard Business Card design.
Sample two-sided design uploaded. White front, Black back.
Would like white shield to be on all black background side.
Willing to look at a couple creative designs, but nothing crazy.
Preference for a classic, confident, strong design.

```html
<!DOCTYPE html>
<html lang="en">
<head>
<meta charset="utf-8">
<title>Veltarum Business Card</title>
<link href="https://fonts.googleapis.com/css2?family=Arimo:wght@400;700&display=swap" rel="stylesheet">
<style>
  :root {
    --backdrop: #969696;
    --card-front: #ffffff;
    --card-back: #27272a;
    --ink-dark: #2b2b2b;
    --ink-mid: #4a4a4a;
    --ink-light: #ffffff;
  }
  html, body {
    margin: 0;
    padding: 0;
    width: 1200px;
    height: 1059px;
    overflow: hidden;
    background: var(--backdrop);
    font-family: "Arimo", Arial, sans-serif;
  }
  .canvas {
    position: relative;
    width: 1200px;
    height: 1059px;
  }
  .card {
    position: absolute;
    width: 690px;
    height: 392px;
  }
  .card--front {
    left: 256px;
    top: 89px;
    background: var(--card-front);
  }
  .card--back {
    left: 253px;
    top: 569px;
    width: 695px;
    height: 394px;
    background: var(--card-back);
  }
  .identity {
    position: absolute;
    right: calc(690px - 303px);
    top: 169px;
    text-align: right;
  }
  .identity__name {
    margin: 0;
    font-weight: 700;
    font-size: 23px;
    color: var(--ink-dark);
    letter-spacing: 0.2px;
    line-height: 1;
  }
  .identity__role {
    margin: 3px 0 0;
    font-size: 18px;
    color: var(--ink-mid);
    line-height: 1;
  }
  .divider {
    position: absolute;
    left: 328px;
    top: 163px;
    width: 1px;
    height: 66px;
    background: var(--ink-dark);
  }
  .contacts {
    position: absolute;
    left: 352px;
    top: 153px;
    margin: 0;
    padding: 0;
    list-style: none;
  }
  .contacts__item {
    display: flex;
    align-items: center;
    height: 27px;
    font-size: 18.5px;
    color: var(--ink-mid);
  }
  .contacts__icon {
    width: 13px;
    height: 13px;
    margin-right: 8px;
    fill: var(--ink-dark);
  }
  .brand {
    position: absolute;
    inset: 0;
    display: flex;
    align-items: center;
    justify-content: center;
    gap: 18px;
  }
  .brand__mark {
    width: 22px;
    height: 22px;
    background: var(--ink-light);
  }
  .brand__name {
    font-weight: 700;
    font-size: 44px;
    letter-spacing: 4px;
    color: var(--ink-light);
    text-transform: uppercase;
  }
</style>
</head>
<body>
<main class="canvas">
  <section class="card card--front" aria-label="Card front">
    <div class="identity">
      <p class="identity__name">DANIEL MARSH</p>
      <p class="identity__role">CEO/Founder</p>
    </div>
    <div class="divider"></div>
    <ul class="contacts">
      <li class="contacts__item">
        <svg class="contacts__icon" viewBox="0 0 16 16" aria-hidden="true"><path d="M3.5 1.5l2.5 3-1.5 2c.9 1.9 2.4 3.4 4.3 4.3l2-1.5 3 2.5-1.6 2.2C6.9 14.2 1.8 9.1 1.3 3.1z"/></svg>
        555-014-2290
      </li>
      <li class="contacts__item">
        <svg class="contacts__icon" viewBox="0 0 16 16" aria-hidden="true"><path d="M1 6l7-5 7 5v9H1zm1.5 1.2V13.5h11V7.2L8 11z"/></svg>
        info@veltarumpartners.com
      </li>
      <li class="contacts__item">
        <svg class="contacts__icon" viewBox="0 0 16 16" aria-hidden="true"><circle cx="8" cy="8" r="7"/><path d="M4 5c1.5 0 2 1 3 1.5s0 2-1 2.5-1 2 0 3.5M10 3c-.5 1 .5 2 1.5 2s1.5 1.5 1 2.5-2 .5-2 2" stroke="#fff" stroke-width="1.2" fill="none"/></svg>
        www.veltarumpartners.com
      </li>
    </ul>
  </section>

  <section class="card card--back" aria-label="Card back">
    <div class="brand">
      <span class="brand__mark" aria-hidden="true"></span>
      <span class="brand__name">Veltarum</span>
    </div>
  </section>
</main>
</body>
</html>
```